I want both print and ebook covers

book title is "The Classroom MEETING HANDBOOK: Fresh Paths to Partner With Families For Student Growth. I want a dark Teal or Navy Background. Yellow and white letters. Distorted Picture of one teacher, two parents and one child around a table or desk. But no Martians! My name should include "Award Winning Author"

Target Market(s)

teachers and other educators--principals, school psychologists, speech therapists, etc.

Industry/Entity Type

schools

Font styles to use
Other font styles liked:
• I just need to see how it looks

Colors
0054AA
0677BA
7BADD7
CADEEF
E8F1F8
0094D4
00A9DD
6FCCEA
C7EBF8
E9F6FB
FFC000
F8CF3A
FAE287
FDF2CF
FEFAEE

Requirements
Must have
• Title top third of page big enough to be read when reduced greatly in size. Contrast so that it "pops'.
Nice to have
• Teacher, two parents and one child around a table/desk. My name should include 'Award winning author'

```html
<!DOCTYPE html>
<html lang="en">
<head>
<meta charset="utf-8">
<title>The Classroom Meeting Handbook – Ebook and Print Covers</title>
<link rel="stylesheet" href="https://fonts.googleapis.com/css2?family=Montserrat:wght@500;600;800;900&family=Titan+One&family=Quicksand:wght@500&display=swap">
<style>
  :root {
    --navy: #1f2069;
    --navy-deep: #191a5c;
    --yellow: #ffd000;
    --white: #ffffff;
    --page: #ffffff;
    --photo-warm: #c9a58a;
    --photo-mid: #8d7a83;
    --photo-cool: #e6e0da;
  }
  * { margin: 0; padding: 0; box-sizing: border-box; }
  html, body {
    width: 1200px; height: 821px; overflow: hidden;
    background: var(--page);
  }
  .stage { position: relative; width: 1200px; height: 821px; }

  .ebook-slot {
    position: absolute; left: 186px; top: 112px;
    width: 363px; height: 545px; overflow: hidden;
  }
  .ebook-slot .cover { transform: scale(0.6636); transform-origin: 0 0; }
  .print-slot {
    position: absolute; left: 653px; top: 0;
    width: 547px; height: 821px;
  }

  .cover {
    position: relative;
    width: 547px; height: 821px;
    background: var(--navy);
    overflow: hidden;
  }
  .cover-art { position: absolute; inset: 0; width: 547px; height: 821px; }
  .title-block {
    position: absolute; top: 36px; left: 0; right: 0;
    text-align: center;
  }
  .title-kicker {
    font-family: "Montserrat", sans-serif; font-weight: 600;
    font-size: 27px; color: var(--yellow); letter-spacing: 0.5px;
    line-height: 1.1;
  }
  .title-main {
    font-family: "Montserrat", sans-serif; font-weight: 900;
    font-size: 84px; color: var(--white); line-height: 0.9;
    letter-spacing: 1px; margin-top: 8px;
  }
  .title-accent {
    font-family: "Titan One", sans-serif;
    font-size: 86px; color: var(--yellow); line-height: 1;
    letter-spacing: -2px; margin-top: 2px;
  }
  .subtitle {
    position: absolute; top: 622px; left: 0; right: 0;
    text-align: center;
    font-family: "Quicksand", sans-serif; font-weight: 500;
    line-height: 1.32; letter-spacing: 0.4px;
  }
  .subtitle-lead { color: var(--yellow); font-size: 29px; }
  .subtitle-rest { color: var(--white); font-size: 27px; }
  .rule {
    position: absolute; left: 110px; width: 327px; height: 1px;
    background: linear-gradient(90deg, transparent, rgba(255,255,255,0.5), transparent);
  }
  .rule-top { top: 617px; }
  .rule-bottom { top: 699px; }
  .author-badge {
    position: absolute; top: 740px; left: 46px;
    width: 455px; height: 50px;
    background: var(--yellow);
    display: flex; align-items: center; justify-content: center;
    font-family: "Montserrat", sans-serif; font-weight: 600;
    font-size: 33px; color: var(--navy); letter-spacing: 0.5px;
  }
</style>
</head>
<body>
<main class="stage">
  <section class="ebook-slot" aria-label="Ebook cover">
    <article class="cover">
      <svg class="cover-art" viewBox="0 0 547 821" xmlns="http://www.w3.org/2000/svg">
        <defs>
          <linearGradient id="ebookPhotoTone" x1="0" y1="0" x2="1" y2="1">
            <stop offset="0" stop-color="var(--photo-cool)"/>
            <stop offset="0.45" stop-color="var(--photo-warm)"/>
            <stop offset="1" stop-color="var(--photo-mid)"/>
          </linearGradient>
        </defs>
        <rect width="547" height="821" fill="var(--navy)"/>
        <path d="M240 296 Q420 282 517 253 L520 282 Q400 294 240 296 Z" fill="var(--yellow)"/>
        <path role="img" aria-label="Photo: a teacher, two parents and a young child talking around a classroom table"
              d="M0 274 Q270 300 547 276 L547 556 Q300 562 0 590 Z" fill="url(#ebookPhotoTone)"/>
        <path d="M30 590 Q300 562 370 560 Q200 575 36 613 Z" fill="var(--yellow)"/>
      </svg>
      <header class="title-block">
        <p class="title-kicker">The Classroom</p>
        <h2 class="title-main">MEETING</h2>
        <p class="title-accent">Handbook</p>
      </header>
      <div class="rule rule-top"></div>
      <p class="subtitle">
        <span class="subtitle-lead">Fresh Paths to Partner</span><br>
        <span class="subtitle-rest">With Families For Student Growth.</span>
      </p>
      <div class="rule rule-bottom"></div>
      <div class="author-badge">Award Winning Author</div>
    </article>
  </section>

  <section class="print-slot" aria-label="Print cover">
    <article class="cover">
      <svg class="cover-art" viewBox="0 0 547 821" xmlns="http://www.w3.org/2000/svg">
        <defs>
          <linearGradient id="printPhotoTone" x1="0" y1="0" x2="1" y2="1">
            <stop offset="0" stop-color="var(--photo-cool)"/>
            <stop offset="0.45" stop-color="var(--photo-warm)"/>
            <stop offset="1" stop-color="var(--photo-mid)"/>
          </linearGradient>
        </defs>
        <rect width="547" height="821" fill="var(--navy)"/>
        <path d="M240 296 Q420 282 517 253 L520 282 Q400 294 240 296 Z" fill="var(--yellow)"/>
        <path role="img" aria-label="Photo: a teacher, two parents and a young child talking around a classroom table"
              d="M0 274 Q270 300 547 276 L547 556 Q300 562 0 590 Z" fill="url(#printPhotoTone)"/>
        <path d="M30 590 Q300 562 370 560 Q200 575 36 613 Z" fill="var(--yellow)"/>
      </svg>
      <header class="title-block">
        <p class="title-kicker">The Classroom</p>
        <h1 class="title-main">MEETING</h1>
        <p class="title-accent">Handbook</p>
      </header>
      <div class="rule rule-top"></div>
      <p class="subtitle">
        <span class="subtitle-lead">Fresh Paths to Partner</span><br>
        <span class="subtitle-rest">With Families For Student Growth.</span>
      </p>
      <div class="rule rule-bottom"></div>
      <div class="author-badge">Award Winning Author</div>
    </article>
  </section>
</main>
</body>
</html>
```